Chiropractic Condition Certificates

Hi,
I'd like have these certificates changed into jpegs with more modern colors and graphics. They need to be eye-catching with good looking images so they will work on Facebook. They need to be suitable to attach in a Facebook post. The current layout might not work for FB post. They may need to be more square then rectangular. Right now they are set up three to a page because In the past they were printed out and handed to patients. I don't need the new ones three to a page. I see these as being used as a jpeg photo in a FB post. Please remove the lines that say "*A $79.00 Value" and the line "MERIDIAN SPINE WELLNESS AND RECOVERY CENTER. 218 HALVERTON AVE. DANBURY, CT 06492 203-555-0187", as they need to be suitable for use by many different chiropractors and not just one.

```html
<!DOCTYPE html>
<html lang="en">
<head>
<meta charset="utf-8">
<title>Sciatic Leg Pain Certificates</title>
<link href="https://fonts.googleapis.com/css2?family=Montserrat:wght@400&family=Roboto+Condensed:wght@400;700&display=swap" rel="stylesheet">
<style>
  :root {
    --page-bg: #ffffff;
    --panel-border: #9aa4ad;
    --panel-light: #e4eef8;
    --panel-mid: #bcd3ea;
    --panel-edge: #8fb1d5;
    --band-dark: #12601a;
    --band-light: #56ad2c;
    --headline-green: #1b7a1f;
    --text-dark: #2b2b2b;
    --text-soft: #3a3a3a;
    --box-border: #0e4f12;
    --white: #ffffff;
    --photo-tone-a: #c9c2b3;
    --photo-tone-b: #8c9a6e;
  }
  * { box-sizing: border-box; margin: 0; padding: 0; }
  html, body {
    width: 1200px; height: 593px; overflow: hidden;
    background: var(--page-bg);
  }
  .canvas { position: relative; width: 1200px; height: 593px; }

  .certificate {
    position: absolute; top: 2px; width: 592px; height: 589px;
    border: 1px solid var(--panel-border);
    background: radial-gradient(ellipse at 50% 45%, var(--panel-light) 0%, var(--panel-mid) 60%, var(--panel-edge) 100%);
    overflow: hidden;
    font-family: "Roboto Condensed", "Arial Narrow", sans-serif;
    color: var(--text-dark);
  }
  .certificate--offer { left: 2px; }
  .certificate--share { left: 605px; }

  .title-band {
    position: absolute; left: 0; right: 0; top: 57px; height: 84px;
    background: linear-gradient(90deg, var(--band-dark) 0%, var(--band-dark) 25%, var(--band-light) 100%);
  }
  .headline {
    position: absolute; left: 182px; top: 16px;
    font-family: "Montserrat", "Century Gothic", sans-serif;
    font-weight: 400; font-size: 31px; line-height: 40px;
    letter-spacing: 0.2px;
  }
  .headline__lead { color: var(--headline-green); display: block; }
  .headline__rest { color: var(--white); display: block; }
  .headline__small { font-size: 22px; }

  .photo-frame {
    position: absolute; left: 18px; top: 32px; width: 155px; height: 151px;
    background: var(--white); padding: 7px;
    box-shadow: 2px 3px 5px rgba(0,0,0,0.45);
  }
  .photo-frame__fill {
    width: 100%; height: 100%;
    background: linear-gradient(135deg, var(--photo-tone-a) 0%, #d8d4c8 45%, var(--photo-tone-b) 100%);
  }

  .intro {
    position: absolute; left: 182px; right: 20px; top: 149px;
    font-size: 16px; line-height: 21px; color: var(--text-soft);
  }
  .body-copy {
    position: absolute; left: 22px; right: 22px;
    font-size: 15.4px; line-height: 20.8px; text-align: justify; color: var(--text-soft);
  }
  .body-copy p + p { margin-top: 9px; }
  .certificate--offer .body-copy { top: 197px; }
  .certificate--share .body-copy { top: 200px; font-size: 16.4px; line-height: 21.3px; left: 24px; right: 24px; }

  .share-line {
    position: absolute; left: 0; right: 0; top: 430px; text-align: center;
    font-weight: 700; font-size: 15.5px; color: var(--headline-green);
  }

  .offer-box {
    position: absolute; display: flex; align-items: center; justify-content: center;
    text-align: center; color: var(--white); font-weight: 700;
    background: linear-gradient(90deg, #17691c 0%, #2f8a24 60%, #46a02a 100%);
    border: 2px solid var(--box-border);
    box-shadow: inset 0 0 0 2px rgba(255,255,255,0.85), 0 0 0 1px rgba(255,255,255,0.6);
  }
  .certificate--offer .offer-box {
    left: 21px; right: 21px; top: 459px; height: 70px;
    font-size: 16px; line-height: 21px;
  }
  .certificate--share .offer-box {
    left: 23px; right: 23px; top: 486px; height: 86px;
    font-size: 23px; line-height: 31px;
  }

  .fine-print {
    position: absolute; left: 28px; right: 24px; top: 539px;
    font-size: 11.3px; line-height: 15px; text-align: justify; color: var(--text-soft);
  }
</style>
</head>
<body>
<div class="canvas">

  <section class="certificate certificate--offer">
    <div class="title-band"></div>
    <div class="photo-frame">
      <div class="photo-frame__fill" role="img" aria-label="Photo of an older man in a green shirt holding his lower back in pain as he rises from a sofa"></div>
    </div>
    <h1 class="headline">
      <span class="headline__lead">HELP SOMEONE</span>
      <span class="headline__rest">WHO HAS</span>
      <span class="headline__rest">SCIATIC LEG PAIN <span class="headline__small">TODAY!</span></span>
    </h1>
    <p class="intro">Your lower back has to a greater amount of stress than your upper back due to the amount of weight it has to support.</p>
    <div class="body-copy">
      <p>As a result, misalignment of the bones of your lower back can occur causing the nerves to be pinched which lead to your hip, leg and foot. This condition is called sciatica. It produces a sharp, burning sensation down your leg. You may experience back and thigh discomfort for weeks or even months before the onset of sciatica. Chiropractic treatment removes the pressure from the pinched nerve by realigning the bones of your spine through gentle Chiropractic adjustments.</p>
      <p>Our mission in Chiropractic is to help people who are tired of just covering up their pain by taking drugs. We can’t reach everyone personally to tell them that Chiropractic may be the answer to their problem. Let’s both offer a helping hand. Refer those you know who could benefit from our care and we will offer our honest and sincere assistance. Give this certificate to someone who we can help together through Chiropractic.</p>
    </div>
    <p class="share-line">Share this certificate to someone who we can help together with Chiropractic.</p>
    <div class="offer-box">THIS GIFT CERTIFICATE IS VALID FOR 2 WEEKS AND ENTITLES THE<br>BEARER TO A CONSULTATION &amp; EXAMINATION AT NO CHARGE.</div>
    <p class="fine-print">The recipient of this Gift Certificate will have NO charge for the first visit services described above. Should treatment be deemed necessary, the usual fees will be explained in advance. This certificate is not valid with Worker’s Comp and Personal Injury cases which often cover 100% of services.</p>
  </section>

  <section class="certificate certificate--share">
    <div class="title-band"></div>
    <div class="photo-frame">
      <div class="photo-frame__fill" role="img" aria-label="Photo of an older man in a green shirt holding his lower back in pain as he rises from a sofa"></div>
    </div>
    <h1 class="headline">
      <span class="headline__lead">HELP SOMEONE</span>
      <span class="headline__rest">WHO HAS</span>
      <span class="headline__rest">SCIATIC LEG PAIN <span class="headline__small">TODAY!</span></span>
    </h1>
    <p class="intro">Your lower back has to a greater amount of stress than your upper back due to the amount of weight it has to support.</p>
    <div class="body-copy">
      <p>As a result, misalignment of the bones of your lower back can occur causing the nerves to be pinched which lead to your hip, leg and foot. This condition is called sciatica. It produces a sharp, burning sensation down your leg. You may experience back and thigh discomfort for weeks or even months before the onset of sciatica. Chiropractic treatment removes the pressure from the pinched nerve by realigning the bones of your spine through gentle Chiropractic adjustments.</p>
      <p>Our mission in Chiropractic is to help people who are tired of just covering up their pain by taking drugs. We can’t reach everyone personally to tell them that Chiropractic may be the answer to their problem. Let’s both offer a helping hand. Refer those you know who could benefit from our care and we will offer our honest and sincere assistance. Give this certificate to someone who we can help together through Chiropractic.</p>
    </div>
    <div class="offer-box">Share this message with someone<br>who we can help together with Chiropractic.</div>
  </section>

</div>
</body>
</html>
```